Buchcover-Design für romanhafte Biografie aus der Nachkriegszeit
Zielgruppe
Meine Zielgruppe sind Leser von Biografien aus der Zeit des Nationalsozialismus bzw. der Nachkriegszeit. Es handelt sich um eine 'romanhafte' Biografie. Ich möchte das Erzählerische betonen. Eigentlich ist es eine Liebesgeschichte.
Aufgabenstellung
Autor: Paul Korvath
Deutscher Titel: Asche und Sehnsucht
Untertitel: Ein stilles Schicksal zwischen zerbrochenen Jahren
Englischer Titel: Ash and Yearning
Untertitel: A quiet fate between broken years
Ich benötige zwei Versionen von demselben Cover: einmal den deutschen Titel, einmal den englischen Titel (keine Hardcoverausgabe)
In meiner romanhaften Biografie aus der Nazi- und Nachkriegszeit beschreibe ich das Leben einer Frau (meiner Mutter), die sich als junges Mädchen in einen jugendlichen Funktionär der Volkswehrjugund verliebt. Er ist mutig, sportlich und unbeschwert - eine Art Siegfried. Die Liebe endet tragisch, da er 1942 in Stalingrad fällt. Da ist die junge Frau achtzehn Jahre alt. (Die Fotos sind aus dieser Zeit.) Ort der Handlung ist Duisburg.
Die junge Frau kann ihre Liebe niemals vergessen, geht aber nach dem Krieg eine neue Beziehung ein. Dieser Mann ist vier Jahre jünger als sie, Mediziner und unbelastet von Kriegserinnerungen. Er ist das Gegenteil ihrer ersten Liebe: Brillenträger, sehr intelligent und ein wenig gefühlskalt.
Die junge Frau steht also zwischen zwei Männern - einem Toten, der für sie nie gestorben ist, und einem Lebenden. Sie steht mit einem Fuß in der alten Zeit (des Nationalsozialismus) und mit dem anderen Fuß in der neuen Zeit.
Text für Buchfalter:
“Es die falsche Zeit, sich zu verlieben”, sagte der Vater. “Und es ist der falsche Mann.”
Aber Hedwig hört nicht auf ihn, denn Willi ist ihre Sandkastenliebe, der Sohn des besten Freundes ihres Vaters. Früh tritt Willi der Volkswehrjugend bei, ihre Freundin Ilse geht zum Kreis Völkischer Töchter. Hedwig ist immer dabei, denn sie liebt Willi und alles, was er ist.
Dann beginnt der Krieg. Hat der Vater doch recht gehabt?

```html
<!DOCTYPE html>
<html lang="de">
<head>
<meta charset="utf-8">
<title>Asche und Sehnsucht – Buchumschlag</title>
<link rel="stylesheet" href="https://fonts.googleapis.com/css2?family=Grenze+Gotisch:wght@800;900&family=Open+Sans:wght@600;700&display=swap">
<style>
  :root {
    --paper-light: #8e7677;
    --paper-mid: #7a6364;
    --paper-dark: #4b3d3c;
    --ground: #231d1b;
    --fog: rgba(170, 150, 150, 0.35);
    --rule: rgba(50, 36, 36, 0.45);
    --sepia-light: #cdb8a8;
    --sepia-mid: #a48b7a;
    --sepia-dark: #3d302b;
    --figure: rgba(28, 22, 20, 0.55);
    --ink: #ffffff;
    --blank: #ffffff;
  }
  * { margin: 0; padding: 0; box-sizing: border-box; }
  html, body { width: 1200px; height: 854px; overflow: hidden; background: var(--paper-dark); }
  .cover {
    position: relative;
    width: 1200px;
    height: 854px;
    overflow: hidden;
    font-family: "Open Sans", Arial, sans-serif;
    color: var(--ink);
  }
  .backdrop {
    position: absolute; inset: 0;
    background:
      radial-gradient(ellipse 35% 22% at 22% 92%, var(--ground) 0%, transparent 75%),
      radial-gradient(ellipse 30% 20% at 62% 95%, var(--ground) 0%, transparent 75%),
      radial-gradient(ellipse 40% 30% at 45% 60%, var(--fog) 0%, transparent 70%),
      linear-gradient(180deg, var(--paper-light) 0%, var(--paper-mid) 50%, #5e4b4a 72%, #352b29 90%, var(--ground) 100%);
  }
  .document-lines, .grain {
    position: absolute; inset: 0;
    width: 1200px; height: 854px;
  }
  .grain { opacity: 0.16; mix-blend-mode: multiply; }
  .soldier-figures {
    position: absolute;
    left: 670px; top: 450px;
    width: 170px; height: 330px;
    background:
      radial-gradient(ellipse 22% 48% at 28% 45%, var(--figure) 0%, transparent 80%),
      radial-gradient(ellipse 26% 50% at 62% 62%, var(--figure) 0%, transparent 80%);
  }
  .portrait {
    position: absolute;
    left: 780px; top: 280px;
    width: 420px; height: 574px;
    background:
      radial-gradient(ellipse 38% 30% at 48% 32%, var(--sepia-light) 0%, rgba(205,184,168,0.7) 55%, transparent 100%),
      radial-gradient(ellipse 60% 55% at 55% 85%, var(--sepia-mid) 0%, var(--sepia-dark) 70%, transparent 100%);
    -webkit-mask-image: radial-gradient(ellipse 62% 70% at 55% 62%, #000 60%, transparent 100%);
    mask-image: radial-gradient(ellipse 62% 70% at 55% 62%, #000 60%, transparent 100%);
  }
  /* back cover */
  .blurb {
    position: absolute;
    left: 112px; top: 108px;
    width: 358px;
    text-align: center;
    font-weight: 600;
    font-size: 13.2px;
    line-height: 19px;
    text-shadow: 0 0 4px rgba(0,0,0,0.45);
  }
  .blurb p + p { margin-top: 19px; }
  .isbn-field {
    position: absolute;
    left: 323px; top: 690px;
    width: 207px; height: 124px;
    background: var(--blank);
  }
  /* spine */
  .spine-author {
    position: absolute;
    left: 589px; top: 92px;
    writing-mode: vertical-rl;
    font-size: 13px;
    font-weight: 600;
    letter-spacing: 0.72em;
  }
  .spine-title {
    position: absolute;
    left: 578px; top: 384px;
    writing-mode: vertical-rl;
    font-family: "Grenze Gotisch", serif;
    font-weight: 900;
    font-size: 40px;
    line-height: 1;
    white-space: nowrap;
  }
  /* front cover */
  .front-title {
    position: absolute;
    left: 690px; top: 32px;
    width: 450px;
    text-align: center;
    font-family: "Grenze Gotisch", serif;
    font-weight: 900;
    line-height: 0.9;
    text-shadow: 0 0 6px rgba(0,0,0,0.25);
  }
  .front-title .line-one { display: block; font-size: 104px; }
  .front-title .line-two { display: block; font-size: 70px; margin-top: 6px; }
  .front-subtitle {
    position: absolute;
    left: 700px; top: 248px;
    width: 430px;
    text-align: center;
    font-weight: 700;
    font-size: 15.5px;
    line-height: 23px;
    text-shadow: 0 0 5px rgba(0,0,0,0.55);
  }
  .front-author {
    position: absolute;
    left: 760px; top: 787px;
    width: 320px;
    text-align: center;
    font-weight: 700;
    font-size: 18px;
    letter-spacing: 0.34em;
    text-shadow: 0 0 5px rgba(0,0,0,0.5);
  }
</style>
</head>
<body>
<main class="cover">
  <div class="backdrop" role="img" aria-label="Sepiafarbene Collage: altes Ausweisdokument mit Stempel und Frakturdruck über nebliger Landschaft"></div>
  <svg class="grain" viewBox="0 0 1200 854" aria-hidden="true">
    <filter id="paper-grain"><feTurbulence type="fractalNoise" baseFrequency="0.9" numOctaves="2" seed="4"/><feColorMatrix type="saturate" values="0"/></filter>
    <rect width="1200" height="854" filter="url(#paper-grain)"/>
  </svg>
  <svg class="document-lines" viewBox="0 0 1200 854" aria-hidden="true">
    <g stroke="var(--rule)" stroke-width="1.5" fill="none">
      <rect x="43" y="12" width="600" height="830"/>
      <line x1="345" y1="12" x2="345" y2="498"/>
      <line x1="43" y1="254" x2="345" y2="254"/>
      <line x1="43" y1="498" x2="643" y2="498"/>
      <line x1="647" y1="8" x2="1200" y2="8"/>
    </g>
  </svg>
  <div class="soldier-figures" role="img" aria-label="Zwei Soldatensilhouetten im Nebel"></div>
  <div class="portrait" role="img" aria-label="Historisches Porträtfoto einer jungen Frau in Mantel mit dunklem Kragen"></div>

  <section class="back-cover">
    <div class="blurb">
      <p>Es die falsche Zeit, sich zu verlieben”, sagte der Vater. “Und es ist der falsche Mann.”</p>
      <p>Aber Hedwig hört nicht auf ihn, denn Willi ist ihre Sandkastenliebe, der Sohn des besten Freundes ihres Vaters. Früh tritt Willi der Volkswehrjugend bei, ihre Freundin Ilse geht zum Kreis Völkischer Töchter. Hedwig ist immer dabei, denn sie liebt Willi und alles, was er ist.</p>
      <p>Dann beginnt der Krieg. Hat der Vater doch recht gehabt?</p>
    </div>
    <div class="isbn-field"></div>
  </section>

  <section class="spine">
    <div class="spine-author">PAUL KORVATH</div>
    <div class="spine-title">Asche und Sehnsucht</div>
  </section>

  <section class="front-cover">
    <h1 class="front-title"><span class="line-one">Asche</span><span class="line-two">und Sehnsucht</span></h1>
    <p class="front-subtitle">Ein stilles Schicksal zwischen<br>zerbrochenen Jahren</p>
    <p class="front-author">PAUL KORVATH</p>
  </section>
</main>
</body>
</html>
```